Art Deco Wedding Invitation

We need a wedding invitation designed for a 1920's Art Deco theme.
The wedding will take place in Berlin, which had a glamorous, modern and wild culture in the 1920's. This may offer some design inspiration.
The couple's names are Rowan and Liesel and the wedding will take place on May 8, 2015.

Industry/Entity Type

Wedding

```html
<!DOCTYPE html>
<html lang="en">
<head>
<meta charset="utf-8">
<title>Rowan and Liesel – Wedding Invitation</title>
<link href="https://fonts.googleapis.com/css2?family=Cormorant+Garamond:ital,wght@1,500&family=Pinyon+Script&display=swap" rel="stylesheet">
<style>
  :root {
    --paper: #ffffff;
    --ink: #111111;
    --gold-deep: #b8902c;
    --gold-mid: #d9b65a;
    --gold-light: #fbf0c4;
  }
  html, body {
    margin: 0;
    padding: 0;
    overflow: hidden;
    background: var(--paper);
  }
  .invitation {
    position: relative;
    width: 877px;
    height: 1200px;
    background: var(--paper);
    overflow: hidden;
  }
  .frame {
    position: absolute;
    inset: 0;
  }
  .figure-art {
    position: absolute;
    left: 0;
    top: 312px;
    width: 330px;
    height: 722px;
    border-radius: 120px 120px 30px 30px;
    background: linear-gradient(90deg, var(--gold-deep), var(--gold-light) 45%, var(--gold-mid) 70%, var(--gold-deep));
  }
  .line {
    position: absolute;
    margin: 0;
    white-space: nowrap;
    transform: translateX(-50%);
    color: var(--ink);
    font-family: "Cormorant Garamond", "Times New Roman", serif;
    font-style: italic;
    font-weight: 500;
    line-height: 1;
  }
  .intro { font-size: 38px; }
  .year { font-family: "Pinyon Script", cursive; font-style: normal; font-size: 52px; }
  .guest { font-size: 28px; }
  .couple {
    font-family: "Pinyon Script", cursive;
    font-style: normal;
    font-size: 66px;
  }
  .details { font-size: 38px; }
  .rule {
    position: absolute;
    left: 378px;
    width: 255px;
    height: 4px;
    background: linear-gradient(90deg, var(--gold-deep), var(--gold-light) 50%, var(--gold-deep));
  }
</style>
</head>
<body>
<main class="invitation">
  <svg class="frame" width="877" height="1200" viewBox="0 0 877 1200" aria-hidden="true">
    <defs>
      <linearGradient id="gold-h" x1="0" x2="1" y1="0" y2="0">
        <stop offset="0" stop-color="#b8902c"/>
        <stop offset="0.5" stop-color="#fbf0c4"/>
        <stop offset="1" stop-color="#b8902c"/>
      </linearGradient>
      <linearGradient id="gold-v" x1="0" x2="0" y1="0" y2="1">
        <stop offset="0" stop-color="#b8902c"/>
        <stop offset="0.5" stop-color="#e8cc7a"/>
        <stop offset="1" stop-color="#b8902c"/>
      </linearGradient>
    </defs>
    <g fill="url(#gold-h)">
      <!-- top bands -->
      <rect x="240" y="30" width="385" height="10"/>
      <rect x="222" y="46" width="403" height="6"/>
      <rect x="205" y="58" width="420" height="5"/>
      <!-- bottom bands -->
      <rect x="240" y="1085" width="385" height="10"/>
      <rect x="222" y="1073" width="403" height="6"/>
      <rect x="205" y="1062" width="420" height="5"/>
      <rect x="240" y="1042" width="385" height="5"/>
      <!-- corner stubs -->
      <rect x="170" y="30" width="12" height="28"/>
      <rect x="170" y="1068" width="12" height="28"/>
    </g>
    <g fill="url(#gold-v)">
      <!-- left stiles -->
      <rect x="185" y="58" width="12" height="1010"/>
      <rect x="205" y="58" width="5" height="250"/>
      <rect x="222" y="46" width="5" height="262"/>
      <rect x="240" y="30" width="6" height="278"/>
      <rect x="205" y="1030" width="5" height="35"/>
      <!-- right stiles -->
      <rect x="736" y="200" width="6" height="735"/>
      <rect x="752" y="200" width="5" height="735"/>
      <rect x="767" y="200" width="5" height="735"/>
      <rect x="782" y="200" width="8" height="735"/>
    </g>
    <!-- corner ornaments -->
    <path role="img" aria-label="Gold corner ornament with daisies" fill="url(#gold-h)"
          d="M620 30 H790 V205 H740 A120 120 0 0 0 620 85 Z"/>
    <path role="img" aria-label="Gold corner ornament with daisies" fill="url(#gold-h)"
          d="M620 1095 H790 V930 H740 A120 120 0 0 1 620 1040 Z"/>
  </svg>

  <div class="figure-art" role="img" aria-label="Illustration of a 1920s bride in a flowing gold gown holding a bouquet of daisies"></div>

  <p class="line intro" style="left:450px; top:160px;">Friends, let’s go back</p>
  <p class="line intro" style="left:450px; top:210px;">the time, glamorous,</p>
  <p class="line intro" style="left:450px; top:258px;">modern and wild ...</p>
  <p class="line year" style="left:468px; top:325px;">1920’s</p>
  <p class="line guest" style="left:488px; top:392px;">Please be our guest as we,</p>

  <div class="rule" style="top:458px;"></div>
  <p class="line couple" style="left:505px; top:472px;">Rowan</p>
  <p class="line couple" style="left:494px; top:538px;">and</p>
  <p class="line couple" style="left:505px; top:605px;">Liesel</p>
  <div class="rule" style="top:681px;"></div>

  <p class="line details" style="left:498px; top:710px;">join together</p>
  <p class="line details" style="left:500px; top:757px;">on May 8, 2015.</p>
  <p class="line details" style="left:498px; top:805px;">Kastanien Chapel</p>
  <p class="line details" style="left:498px; top:852px;">Lindenblatt Road</p>
  <p class="line details" style="left:502px; top:900px;">Berlin, Germany</p>
</main>
</body>
</html>
```